Corporate Travel Technology Company needs new Business Card design

We need a new business card design to reflect our re-branded company. Our company is called velomOx (pronounced zephyra) and we provide Business Intelligence and mobile travel management solutions for the corporate travel industry. Our multinational customers use our solutions to manage large travel budgets and frequent travellers, as well as to save money and reduce risk. We'd like to see designs that use the blue and green palette as well as our corporate logo (attached below). The design should communicate innovation, insight, forward thinking, contemporary, trusted.

Target Market(s)

Large multinational corporates and Travel Agencies.

Industry/Entity Type

Business

Contact Information for Business Card

Marguerite Ollen
Chief Executive
velomOx
Phone number - +61 (0)2 9000 4178
Email address - marguerite.ollen@velomox.example
Mobile number - +61 (0)400 516 042
www.velomox.example

Font styles to use
Other font styles liked:
• Please use font as close to corporate logo as possible

Colors
0255a3
0393ce
00a990
33b8a4
33a6d7
3176b5

Requirements
Must have
• Please include the words;
• Mobile Travel Management
• Accelerating Travel Business Insights
• Use corporate logo - although icon can be stylised if needed

```html
<!DOCTYPE html>
<html lang="en">
<head>
<meta charset="utf-8">
<title>velomOx business card</title>
<link rel="stylesheet" href="https://fonts.googleapis.com/css2?family=Quicksand:wght@500;600&family=Open+Sans:wght@400&family=Libre+Baskerville:ital@1&display=swap">
<style>
  :root {
    --page-bg: #1f1f21;
    --card-teal: #23b9a5;
    --band-blue: #2a6fb6;
    --ink-white: #ffffff;
    --icon-blue: #2a6fb6;
  }
  html, body {
    margin: 0;
    width: 1200px;
    height: 1000px;
    overflow: hidden;
    background: var(--page-bg);
  }
  .canvas {
    position: relative;
    width: 1200px;
    height: 1000px;
  }
  .card {
    position: absolute;
    left: 250px;
    width: 700px;
    height: 400px;
    background: var(--card-teal);
    color: var(--ink-white);
    overflow: hidden;
  }
  .card--contact { top: 50px; }
  .card--brand { top: 550px; }

  /* contact side */
  .side-band {
    position: absolute;
    left: 0; top: 0; bottom: 0;
    width: 110px;
    background: var(--band-blue);
  }
  .icon-badge {
    position: absolute;
    left: 36px;
    width: 38px;
    height: 38px;
    border-radius: 50%;
    background: var(--ink-white);
    display: flex;
    align-items: center;
    justify-content: center;
  }
  .icon-badge svg { width: 20px; height: 20px; }
  .icon-badge--phone { top: 228px; }
  .icon-badge--web { top: 286px; }
  .icon-badge--mail { top: 344px; }

  .contact-block {
    position: absolute;
    left: 140px;
    top: 26px;
    font-family: "Open Sans", Arial, sans-serif;
    font-size: 21px;
    line-height: 1.2;
  }
  .contact-name { margin: 0; font-size: 22px; font-weight: 400; }
  .contact-title {
    margin: 0 0 0 70px;
    font-family: "Libre Baskerville", Georgia, serif;
    font-style: italic;
    font-size: 15px;
  }
  .contact-company { margin: 0 0 0 92px; font-size: 21px; }
  .contact-phones { margin: 30px 0 0 0; }
  .contact-phones p { margin: 0; }
  .contact-web { margin: 34px 0 0 0; font-size: 22px; }
  .contact-mail { margin: 30px 0 0 0; font-size: 22px; }

  /* brand side */
  .brand-name {
    position: absolute;
    right: 60px;
    top: 92px;
    margin: 0;
    font-family: "Quicksand", Arial, sans-serif;
    font-weight: 600;
    font-size: 88px;
    line-height: 1;
    letter-spacing: 4px;
    text-transform: uppercase;
  }
  .brand-taglines {
    position: absolute;
    right: 60px;
    top: 232px;
    text-align: right;
    font-family: "Quicksand", Arial, sans-serif;
    font-weight: 600;
    font-size: 27px;
    line-height: 1.45;
  }
  .brand-taglines p { margin: 0; }
</style>
</head>
<body>
<main class="canvas">

  <section class="card card--contact" aria-label="Contact side">
    <div class="side-band">
      <span class="icon-badge icon-badge--phone">
        <svg viewBox="0 0 24 24" aria-hidden="true"><path fill="var(--icon-blue)" d="M6.6 10.8a15.1 15.1 0 0 0 6.6 6.6l2.2-2.2a1 1 0 0 1 1-.25 11.4 11.4 0 0 0 3.6.57 1 1 0 0 1 1 1V20a1 1 0 0 1-1 1A17 17 0 0 1 3 4a1 1 0 0 1 1-1h3.5a1 1 0 0 1 1 1c0 1.25.2 2.46.57 3.6a1 1 0 0 1-.25 1z"/></svg>
      </span>
      <span class="icon-badge icon-badge--web">
        <svg viewBox="0 0 24 24" aria-hidden="true" fill="none" stroke="var(--icon-blue)" stroke-width="1.6"><circle cx="12" cy="12" r="9"/><ellipse cx="12" cy="12" rx="4" ry="9"/><path d="M3 12h18M4.5 7.5h15M4.5 16.5h15"/></svg>
      </span>
      <span class="icon-badge icon-badge--mail">
        <svg viewBox="0 0 24 24" aria-hidden="true"><text x="12" y="17" text-anchor="middle" font-family="Open Sans, Arial, sans-serif" font-size="16" fill="var(--icon-blue)">@</text></svg>
      </span>
    </div>

    <div class="contact-block">
      <p class="contact-name">Marguerite Ollen</p>
      <p class="contact-title">Chief Executive</p>
      <p class="contact-company">velomOx</p>
      <div class="contact-phones">
        <p>+61 (0)2 9000 4178</p>
        <p>+61 (0)400 516 042</p>
      </div>
      <p class="contact-web">www.velomox.example</p>
      <p class="contact-mail">marguerite.ollen@velomox.example</p>
    </div>
  </section>

  <section class="card card--brand" aria-label="Brand side">
    <p class="brand-name">velomOx</p>
    <div class="brand-taglines">
      <p>Mobile Travel Management</p>
      <p>Accelerating Travel Business Insights</p>
    </div>
  </section>

</main>
</body>
</html>
```